Delia Forsby Space Tamer

a larger business card may standard size 4” x 9” describing what I do. I don’t know if this would be considered a flyer. I rearrange, redesign and stage houses for the owner or to sell.

```html
<!DOCTYPE html>
<html lang="en">
<head>
<meta charset="utf-8">
<title>Delia Forsby – Space Tamer Card</title>
<link rel="stylesheet" href="https://fonts.googleapis.com/css2?family=Montserrat:wght@400;500;600&family=Roboto:wght@400;700&display=swap">
<style>
  :root {
    --backdrop: #3a3a3a;
    --card: #ffffff;
    --ink: #111111;
    --teal: #5fc3bd;
    --teal-deep: #2a8f88;
    --dot: #0e4a46;
    --red: #e3342f;
    --sky: #63c7c0;
    --adobe: #e8864a;
    --earth: #8a6a55;
    --ground: #c9b9a8;
  }
  * { margin: 0; padding: 0; box-sizing: border-box; }
  html, body { width: 900px; height: 1200px; overflow: hidden; }
  body { background: var(--backdrop); position: relative; font-family: "Montserrat", sans-serif; color: var(--ink); }

  .card { position: absolute; top: 128px; width: 420px; height: 945px; background: var(--card); overflow: hidden; }
  .card--front { left: 23px; }
  .card--back { left: 461px; width: 419px; }

  .hero-photo {
    position: absolute; left: 0; top: 0; width: 100%; height: 372px;
    background: linear-gradient(180deg, var(--sky) 0%, var(--sky) 38%, #b7a08a 47%, var(--adobe) 60%, #b86a3c 82%, var(--ground) 100%);
  }
  .portrait {
    position: absolute; left: 121px; top: 284px; width: 176px; height: 176px;
    border-radius: 50%; border: 6px solid var(--card);
    background: radial-gradient(circle at 50% 45%, #d8c9c2 0%, #9fcfcb 50%, #1aa39a 100%);
  }

  .front-text { position: absolute; left: 0; width: 100%; text-align: center; }
  .name { font-weight: 500; font-size: 35px; letter-spacing: 0.5px; line-height: 1; }
  .front .name { top: 497px; }
  .front-subtitle { top: 533px; font-size: 20px; color: var(--teal); letter-spacing: 0.5px; }
  .services-title { top: 594px; font-size: 21px; font-weight: 500; }
  .services { top: 622px; font-size: 17.5px; }
  .services .dot { color: var(--dot); padding: 0 4px; }
  .tagline { top: 649px; font-family: Arial, sans-serif; font-size: 14.5px; line-height: 20px; color: var(--teal-deep); }
  .divider { top: 692px; font-size: 18px; font-weight: 600; }
  .contact { top: 716px; font-size: 17.5px; line-height: 26px; }

  .back-name { position: absolute; top: 112px; left: 0; width: 100%; text-align: center; font-size: 31px; }
  .back-subtitle { position: absolute; top: 147px; left: 0; width: 100%; text-align: center; font-size: 17px; color: var(--teal-deep); letter-spacing: 0.5px; }
  .body-copy { position: absolute; left: 0; width: 100%; text-align: center; font-family: "Roboto", sans-serif; font-size: 14.5px; line-height: 24px; }
  .accent { color: var(--red); }
  .footer-photo {
    position: absolute; left: 0; bottom: 0; width: 100%; height: 205px;
    background: linear-gradient(180deg, #ffffff 0%, #cfd6d8 18%, #a58d7a 34%, var(--adobe) 52%, #a9643c 72%, var(--ground) 100%);
  }
</style>
</head>
<body>
  <section class="card card--front front">
    <div class="hero-photo" role="img" aria-label="Photo of an orange adobe house with desert mountains under a teal sky"></div>
    <div class="portrait" role="img" aria-label="Portrait photo of Delia Forsby"></div>
    <h1 class="front-text name">DELIA FORSBY</h1>
    <p class="front-text front-subtitle">(A SPACE TAMER)</p>
    <h2 class="front-text services-title">HOMES</h2>
    <p class="front-text services">Rearranged<span class="dot">•</span>Redesigned<span class="dot">•</span>Staged to Sell</p>
    <p class="front-text tagline">With Little or no cost, delia breathes new life<br>&amp; energy into your home</p>
    <p class="front-text divider">–</p>
    <p class="front-text contact">dforsby@mailbay.net<br>555-01-09<br>1420 S. Marlow Drive. Dunmore, AZ 853</p>
  </section>

  <section class="card card--back">
    <h1 class="name back-name">DELIA FORSBY</h1>
    <p class="back-subtitle">A SPACE TAMER</p>
    <p class="body-copy" style="top:189px">For 36 years, Delia was a real estate Broker in Oregon.<br>She has a track record of transforming houses<br>that do not sell into homes that sell quickly.</p>
    <p class="body-copy accent" style="top:273px">As a Hearth &amp; Garden Living national award winner,</p>
    <p class="body-copy" style="top:303px">Her talent has not gone unnoticed</p>
    <p class="body-copy" style="top:362px">She eagerly finds renewed energy by rearranging what you<br>already have, and rethinking your space.</p>
    <p class="body-copy" style="top:440px">With a dash of this, a zest of that,<br>she virtually re-invigorates your environment,</p>
    <p class="body-copy" style="top:525px">Thrilled customers say...</p>
    <p class="body-copy accent" style="top:553px">“This is just how I dreamed my home would look !”</p>
    <p class="body-copy" style="top:581px">Make your space livable, lovable and <strong>Profitable...</strong><br>...a place where you or your buyer can hardly wait to<br>come home to. Voila!</p>
    <div class="footer-photo" role="img" aria-label="Photo of the adobe house with desert mountains fading into white"></div>
  </section>
</body>
</html>
```